job vacancy cover page

I need to design a one pager for a job I'd like to apply for. The one I have done looks shit and amateur!! Wanting it to look amazing and professional (Not too professional though as they are pretty young and fun).

```html
<!DOCTYPE html>
<html lang="en">
<head>
<meta charset="utf-8">
<title>Bright Harbour – Cover Page</title>
<link href="https://fonts.googleapis.com/css2?family=Oswald:wght@400;500;600&family=Poppins:wght@400;500;600;700&display=swap" rel="stylesheet">
<style>
:root{
  --navy:#1c2b45;
  --red:#d7193a;
  --sky-deep:#7cc3d2;
  --sky-light:#a9e5ee;
  --rust-dark:#6f372d;
  --rust:#8b4a38;
  --line:#8a3b2f;
  --text:#2a2a2a;
  --white:#ffffff;
  --teal:#2f9c9a;
}
*{margin:0;padding:0;box-sizing:border-box}
html,body{width:1200px;height:2881px;overflow:hidden;background:var(--white)}
body{position:relative;font-family:'Poppins',sans-serif;color:var(--text)}
.abs{position:absolute}
.display{font-family:'Oswald',sans-serif;font-weight:500;text-transform:uppercase;letter-spacing:.5px}

/* header */
.site-header{left:0;top:0;width:1200px;height:80px;background:var(--white)}
.brand{left:74px;top:20px;font-family:'Oswald',sans-serif;font-size:31px;font-weight:400;color:var(--navy);text-transform:uppercase;letter-spacing:.5px}
.social{left:816px;top:30px;display:flex;gap:20px}
.social span{width:20px;height:20px;border-radius:50%;background:var(--red)}
.menu{left:1052px;top:30px;display:flex;align-items:center;gap:9px;font-size:15px;color:var(--navy)}
.menu i{display:block;width:20px;height:3px;background:var(--navy);box-shadow:0 -7px 0 var(--navy),0 7px 0 var(--navy)}

/* hero */
.hero{left:0;top:80px;width:1200px;height:588px;background:linear-gradient(100deg,var(--sky-deep) 0%,#86cbd9 45%,var(--sky-light) 100%)}
.hero-art{left:515px;top:100px;width:660px;height:568px;background:radial-gradient(ellipse at 60% 50%,rgba(215,25,58,.35) 0%,rgba(28,43,69,.25) 45%,rgba(169,229,238,0) 72%)}
.hero-title{left:72px;top:218px;font-size:62px;color:var(--navy);line-height:1}
.hero-sub{left:76px;top:304px;font-size:26px;font-weight:700;color:var(--red)}
.powers{left:76px;top:352px;list-style:none}
.powers li{display:flex;align-items:center;gap:12px;height:45.3px;font-size:22px;color:var(--white)}

/* why */
.why-title{left:0;top:724px;width:1200px;text-align:center;font-size:52px;color:var(--navy)}
.connectors{left:0;top:0}
.frame{border:2px solid var(--navy);background:var(--white)}
.frame .art{position:absolute;left:28px;top:28px;right:28px;bottom:28px;border-radius:6px}
.art-desk{background:linear-gradient(135deg,#e8f6f5 0%,#8fd0cb 55%,#1f6d6e 100%)}
.art-call{background:linear-gradient(160deg,#c6e7e4 0%,#2a6f80 70%,#e79a3a 100%)}
.art-team{background:linear-gradient(135deg,#f3a23b 0%,#f08a86 40%,#2c9d9a 75%,#1d5571 100%)}
.sec-title{font-size:35px;color:var(--red)}
.list{list-style:none}
.list li{display:flex;align-items:center;gap:16px;height:48px;font-size:18px;color:var(--text)}
.list svg{flex:none}
.project h3{font-size:24px;font-weight:600;color:#333;line-height:1.3}
.project p{font-size:18px;line-height:1.45;color:#333;margin-bottom:14px;width:370px}

/* success / passion */
.band-left{left:0;top:2254px;width:602px;height:462px;background:var(--rust-dark)}
.band-right{left:602px;top:2254px;width:598px;height:462px;background:var(--rust)}
.band-deco{opacity:.12;background:var(--white)}
.band-title{font-size:52px;color:var(--white)}
.check-row{display:flex;align-items:center}
.check-row .ring{width:60px;height:60px;border:2px solid var(--white);border-radius:50%;display:flex;align-items:center;justify-content:center;flex:none}
.check-row p{font-size:15.5px;line-height:1.7;color:var(--white);margin-left:27px}

/* footer */
.foot-nav{left:0;top:2749px;width:1200px;display:flex;justify-content:center;gap:40px;font-size:17px;font-weight:600;color:var(--navy)}
.copyright{left:0;top:2796px;width:1200px;text-align:center;font-size:15px;color:var(--navy)}
.legal{left:0;top:2827px;width:1200px;text-align:center;font-size:15px;color:var(--navy)}
</style>
</head>
<body>

<header class="abs site-header">
  <div class="abs brand">Bright Harbour</div>
  <div class="abs social" aria-label="Social links"><span></span><span></span><span></span><span></span><span></span></div>
  <div class="abs menu"><i></i>MENU</div>
</header>

<section class="abs hero">
</section>
<div class="abs hero-art" role="img" aria-label="Illustration of a flying businesswoman superhero with a red cape and briefcase"></div>
<svg class="abs" style="left:0;top:80px" width="1200" height="588" aria-hidden="true">
  <path d="M430 0 C520 150 610 300 640 588" stroke="#fff" stroke-opacity=".6" stroke-width="2" fill="none"/>
  <path d="M480 0 C560 140 640 280 650 480 C655 520 600 440 560 430 C520 420 540 520 600 588" stroke="#fff" stroke-opacity=".6" stroke-width="2" fill="none"/>
  <path d="M770 0 C900 60 1050 120 1200 130" stroke="#fff" stroke-opacity=".6" stroke-width="2" fill="none"/>
</svg>
<h1 class="abs display hero-title">If I was a superhero</h1>
<div class="abs hero-sub">My four superpowers would be:</div>
<ul class="abs powers">
  <li><svg width="22" height="18" viewBox="0 0 22 18"><path d="M2 9 L8 15 L20 2" stroke="#fff" stroke-width="4" fill="none"/></svg>Proactiveness</li>
  <li><svg width="22" height="18" viewBox="0 0 22 18"><path d="M2 9 L8 15 L20 2" stroke="#fff" stroke-width="4" fill="none"/></svg>Creativity</li>
  <li><svg width="22" height="18" viewBox="0 0 22 18"><path d="M2 9 L8 15 L20 2" stroke="#fff" stroke-width="4" fill="none"/></svg>Pride in my work</li>
  <li><svg width="22" height="18" viewBox="0 0 22 18"><path d="M2 9 L8 15 L20 2" stroke="#fff" stroke-width="4" fill="none"/></svg>Organisational skills</li>
</ul>

<h2 class="abs display why-title">Why Bright Harbour?</h2>

<svg class="abs connectors" width="1200" height="2881" aria-hidden="true">
  <g stroke="var(--line)" stroke-width="1.6" fill="none">
    <path d="M587 1083 H544 V1255 H717 V1213"/>
    <path d="M479 1286 V1243 H652 V1416 H612"/>
    <path d="M612 1545 H652 V1719 H479 V1671"/>
    <path d="M587 1878 H544 V1706 H717 V1742"/>
  </g>
</svg>

<div class="abs frame" style="left:587px;top:829px;width:449px;height:384px">
  <div class="art art-desk" role="img" aria-label="Illustration of a person working at a computer surrounded by ideas and charts"></div>
</div>
<div class="abs frame" style="left:163px;top:1286px;width:449px;height:385px">
  <div class="art art-call" role="img" aria-label="Illustration of a laptop showing a video call with a team"></div>
</div>
<div class="abs frame" style="left:587px;top:1742px;width:449px;height:385px">
  <div class="art art-team" role="img" aria-label="Illustration of a connected team collaborating on projects"></div>
</div>

<h3 class="abs display sec-title" style="left:163px;top:864px">Values that stood out</h3>
<ul class="abs list" style="left:163px;top:920px">
  <li><svg width="15" height="12" viewBox="0 0 15 12"><path d="M1 1 L6 6 L1 11 M8 1 L13 6 L8 11" stroke="#222" stroke-width="2.2" fill="none"/></svg>Change for the better</li>
  <li><svg width="15" height="12" viewBox="0 0 15 12"><path d="M1 1 L6 6 L1 11 M8 1 L13 6 L8 11" stroke="#222" stroke-width="2.2" fill="none"/></svg>Excellence – not mediocre</li>
  <li><svg width="15" height="12" viewBox="0 0 15 12"><path d="M1 1 L6 6 L1 11 M8 1 L13 6 L8 11" stroke="#222" stroke-width="2.2" fill="none"/></svg>Put your heart into it and give a shit</li>
  <li><svg width="15" height="12" viewBox="0 0 15 12"><path d="M1 1 L6 6 L1 11 M8 1 L13 6 L8 11" stroke="#222" stroke-width="2.2" fill="none"/></svg>Going the extra mile</li>
  <li><svg width="15" height="12" viewBox="0 0 15 12"><path d="M1 1 L6 6 L1 11 M8 1 L13 6 L8 11" stroke="#222" stroke-width="2.2" fill="none"/></svg>Take risks</li>
</ul>

<h3 class="abs display sec-title" style="left:691px;top:1340px">What you offer</h3>
<ul class="abs list" style="left:691px;top:1395px">
  <li><svg width="15" height="12" viewBox="0 0 15 12"><path d="M1 1 L6 6 L1 11 M8 1 L13 6 L8 11" stroke="#222" stroke-width="2.2" fill="none"/></svg>Learning &amp; Developing</li>
  <li><svg width="15" height="12" viewBox="0 0 15 12"><path d="M1 1 L6 6 L1 11 M8 1 L13 6 L8 11" stroke="#222" stroke-width="2.2" fill="none"/></svg>Team</li>
  <li><svg width="15" height="12" viewBox="0 0 15 12"><path d="M1 1 L6 6 L1 11 M8 1 L13 6 L8 11" stroke="#222" stroke-width="2.2" fill="none"/></svg>Flexibility</li>
  <li><svg width="15" height="12" viewBox="0 0 15 12"><path d="M1 1 L6 6 L1 11 M8 1 L13 6 L8 11" stroke="#222" stroke-width="2.2" fill="none"/></svg>Fun</li>
</ul>

<h3 class="abs display sec-title" style="left:163px;top:1753px">Interesting projects</h3>
<div class="abs project" style="left:163px;top:1815px">
  <h3>Corvanta</h3>
  <p>Leadership development and team effectiveness</p>
  <h3>Halbrook</h3>
  <p>Change management for true transformation</p>
  <h3>Marlow &amp; Finch</h3>
  <p>Customer centricity at Australia's most iconic department store</p>
</div>

<section class="abs band-left"></section>
<section class="abs band-right"></section>
<div class="abs band-deco" style="left:325px;top:2400px;width:270px;height:310px;border-radius:40px 40px 20px 20px" role="img" aria-label="Faint trophy decoration"></div>
<div class="abs band-deco" style="left:880px;top:2400px;width:315px;height:310px;border-radius:50% 50% 50% 50%/45% 45% 55% 55%" role="img" aria-label="Faint heart decoration"></div>

<h2 class="abs display band-title" style="left:75px;top:2318px">Some of my success</h2>
<div class="abs" style="left:75px;top:2402px">
  <div class="check-row" style="height:86px"><span class="ring"><svg width="24" height="18" viewBox="0 0 24 18"><path d="M2 9 L9 16 L22 2" stroke="#fff" stroke-width="4" fill="none"/></svg></span><p>Increased client workshops by 85%<br>across accounts.</p></div>
  <div class="check-row" style="height:86px"><span class="ring"><svg width="24" height="18" viewBox="0 0 24 18"><path d="M2 9 L9 16 L22 2" stroke="#fff" stroke-width="4" fill="none"/></svg></span><p>Delivered double digit revenue increase.</p></div>
  <div class="check-row" style="height:86px"><span class="ring"><svg width="24" height="18" viewBox="0 0 24 18"><path d="M2 9 L9 16 L22 2" stroke="#fff" stroke-width="4" fill="none"/></svg></span><p>Re-designed workshops for virtual delivery,<br>maintaining key relationships.</p></div>
</div>

<h2 class="abs display band-title" style="left:644px;top:2318px">Passion</h2>
<div class="abs" style="left:643px;top:2402px">
  <div class="check-row" style="height:86px"><span class="ring"><svg width="24" height="18" viewBox="0 0 24 18"><path d="M2 9 L9 16 L22 2" stroke="#fff" stroke-width="4" fill="none"/></svg></span><p>The development of others and / or<br>their teams.</p></div>
  <div class="check-row" style="height:86px"><span class="ring"><svg width="24" height="18" viewBox="0 0 24 18"><path d="M2 9 L9 16 L22 2" stroke="#fff" stroke-width="4" fill="none"/></svg></span><p>Helping people learn and be successful in life<br>and in their careers.</p></div>
  <div class="check-row" style="height:86px"><span class="ring"><svg width="24" height="18" viewBox="0 0 24 18"><path d="M2 9 L9 16 L22 2" stroke="#fff" stroke-width="4" fill="none"/></svg></span><p>Exceptional client experiences</p></div>
</div>

<nav class="abs foot-nav"><span>Home</span><span>About Us</span><span>Services</span><span>Why Bright Harbour</span><span>Contact Us</span></nav>
<div class="abs copyright">Copyright © 2022.CompanyName&nbsp; All Right Reserved</div>
<div class="abs legal">Privacy &nbsp;|&nbsp; Terms of Use</div>

</body>
</html>
```